A book about police officer shootings needs a dynamic cover design

I've almost completed a book on officer involved shootings...a very hot topic today. The title is "R.K.T. Beyond The Silence Fell." (emphasis on "beyond the silence") It details three separate shooting incidents, all within the same law enforcement family.I need a professional looking book cover that helps capture the drama. I attached a file of something I put together that is close, but I am concerned about "readability" and want a more professional look. I included a photo that I took off the internet of a gun being shot. That particular photo can stay or go, or be altered, but I like the perspective of the photo being fired from the person behind it. I wanted the cover to have the characteristics and color of a police uniform, utilizing blues, silvers, and maybe a little gold. I'm concerned about making sure the font and colors are also easy to read. I also will be working on a website design for "Beyond The Silence.Com" once the book hits the market. The back cover will incorporate the same colors, but only be a picture and excerpts from the book. I've included both for your review.

Target Market(s)

Law Enforcement, Christian, Media

Font styles to use
Sans Serif

Requirements
Must have
• A professional and readable appearance, that captures the drama of the topic. All the wording on the sample cover I attached, unless you come up with something better. A gun being fired from the perspective of the officer pulling the trigger. The size of the book will be the standard 6 x 9 in size. "Beyond The Silence" will eventually be my website domain and social media promotion hashtag.
Nice to have
• I would like the cover to incorporate the colors of a police uniform and badge, traditionally, navy blue, silver and some gold.
Should not have
• No police badge with a black band across. Not my topic.

```html
<!DOCTYPE html>
<html lang="en">
<head>
<meta charset="utf-8">
<title>R.K.T. Beyond The Silence Fell – Cover Spread</title>
<link href="https://fonts.googleapis.com/css2?family=Oswald:wght@500;600&family=Montserrat:wght@500;600;700&display=swap" rel="stylesheet">
<style>
  :root {
    --bg: #2a2622;
    --navy-deep: #0b1526;
    --navy: #14253e;
    --steel-blue: #3d5f80;
    --mist: #7c98b3;
    --silver-light: #f1f4f7;
    --silver: #b9c3cc;
    --silver-dark: #6e7a86;
    --gold: #f5c04a;
    --gold-deep: #c9781c;
    --white: #ffffff;
  }
  * { box-sizing: border-box; margin: 0; padding: 0; }
  html, body { width: 1200px; height: 800px; overflow: hidden; }
  body {
    background: var(--bg);
    display: flex;
    align-items: center;
    justify-content: center;
    font-family: "Montserrat", sans-serif;
    color: var(--white);
  }
  .spread { display: flex; height: 720px; box-shadow: 0 10px 40px rgba(0,0,0,.5); }

  /* Back cover */
  .back-cover {
    width: 480px; height: 720px; position: relative;
    background:
      radial-gradient(ellipse at 60% 45%, rgba(124,152,179,.45), transparent 60%),
      linear-gradient(160deg, var(--navy-deep) 0%, var(--navy) 45%, var(--steel-blue) 70%, var(--navy-deep) 100%);
  }
  .back-frame {
    position: absolute; left: 40px; top: 52px; width: 400px; height: 640px;
    border: 5px solid var(--silver);
    outline: 1px solid var(--silver-dark);
    box-shadow: inset 0 0 0 2px var(--silver-dark), 0 0 8px rgba(0,0,0,.6);
    border-radius: 6px;
    background: rgba(11,21,38,.35);
    padding: 16px 20px;
    text-align: center;
  }
  .tagline { font-weight: 600; font-size: 13px; line-height: 1.3; letter-spacing: .3px; }
  .family-photo {
    display: block; width: 170px; height: 230px; margin: 12px auto 8px;
    background: linear-gradient(180deg, #8fb0cf 0%, #d7dde2 35%, #5a5040 70%, #1c1f26 100%);
  }
  .photo-caption { display: flex; justify-content: center; gap: 12px; font-size: 8.5px; font-weight: 700; margin-bottom: 10px; }
  .story-title {
    font-size: 11px; font-weight: 700; font-variant: small-caps; text-decoration: underline;
    margin: 8px 0 4px;
  }
  .excerpt { font-size: 9.5px; line-height: 1.42; font-variant: small-caps; font-weight: 600; }

  /* Spine */
  .spine {
    width: 80px; height: 720px;
    background: linear-gradient(180deg, var(--navy-deep) 0%, var(--navy) 40%, var(--steel-blue) 70%, var(--navy-deep) 100%);
    display: flex; justify-content: center; align-items: flex-start; padding-top: 40px;
  }
  .spine-title {
    writing-mode: vertical-rl;
    font-family: "Montserrat", sans-serif; font-weight: 700;
    font-size: 30px; letter-spacing: 2px; font-variant: small-caps;
    color: var(--white); white-space: nowrap;
  }

  /* Front cover */
  .front-cover {
    width: 480px; height: 720px; position: relative; overflow: hidden;
    background: linear-gradient(170deg, var(--steel-blue) 0%, var(--navy) 45%, var(--steel-blue) 75%, var(--navy-deep) 100%);
  }
  .cover-art {
    position: absolute; inset: 0;
    background:
      radial-gradient(circle at 18% 12%, rgba(255,230,150,.95) 0%, rgba(245,192,74,.7) 10%, rgba(201,120,28,.35) 22%, transparent 40%),
      radial-gradient(ellipse at 75% 35%, rgba(20,37,62,.8), transparent 60%),
      linear-gradient(170deg, #5d7d9c 0%, #233a58 45%, #3a5878 75%, #0e1a2e 100%);
  }
  .title-block { position: absolute; left: 0; right: 0; top: 110px; text-align: center; }
  .title-block span {
    display: block; font-family: "Oswald", sans-serif; font-weight: 600;
    background: linear-gradient(180deg, var(--silver-light) 0%, var(--silver) 45%, var(--silver-dark) 55%, var(--silver-light) 100%);
    -webkit-background-clip: text; background-clip: text; color: transparent;
    filter: drop-shadow(1px 2px 2px rgba(0,0,0,.7));
    line-height: 1;
  }
  .title-initials { font-size: 130px; font-weight: 500; letter-spacing: -2px; }
  .title-line-1 { font-size: 104px; letter-spacing: 4px; margin-top: 8px; }
  .title-line-2 { font-size: 96px; letter-spacing: 4px; }
  .title-line-3 { font-size: 78px; letter-spacing: 3px; }
  .title-line-4 { font-size: 78px; letter-spacing: 3px; }
  .author-row { position: absolute; left: 20px; bottom: 52px; display: flex; align-items: center; gap: 10px; }
  .badge-shape { width: 104px; height: 118px; }
  .author-name {
    font-family: "Oswald", sans-serif; font-weight: 500; font-size: 40px; letter-spacing: 2px;
    color: var(--silver); margin-top: 48px;
  }
</style>
</head>
<body>
  <main class="spread">
    <section class="back-cover">
      <div class="back-frame">
        <p class="tagline">“YOU CANNOT RELY ON ANYONE BUT<br>YOURSELF TO SAVE YOUR LIFE…”</p>
        <div class="family-photo" role="img" aria-label="Photo of the three officers of the Kessler family standing together outdoors"></div>
        <div class="photo-caption"><span>LT. RAY KESSLER</span><span>DANA KESSLER</span><span>COLE KESSLER</span></div>

        <h3 class="story-title">Ray’s Story</h3>
        <p class="excerpt">“And then I heard it. The unmistakable sound of a shotgun being racked. And then another one. I was hit with near-binding light from police flashlights, but was still able to make out the silhouettes of officers taking cover behind their patrol car doors… All weapons pointed directly at me…”</p>

        <h3 class="story-title">Dana’s Story</h3>
        <p class="excerpt">“Dana stood over him, holding the shotgun in his left hand and his now empty handgun in his right. He stood there in stunned disbelief at how a routine call had escalated into a violent confrontation in a matter of seconds. The stench emanating from the house, mixed with the smell of gunpowder and blood, was almost overwhelming.”</p>

        <h3 class="story-title">Cole’s Story</h3>
        <p class="excerpt">“Cole desperately wanted to stay with Mark, but the danger still presented by Harlow was paramount. As Cole rushed towards the suspended vehicle, the door suddenly opened. Harlow climbed out and dropped to the ground. He stood and faced Cole like a raging bull. If the bull charged, Cole was prepared to shoot again…”</p>
      </div>
    </section>

    <section class="spine">
      <h2 class="spine-title">R.K.T. Beyond The Silence Fell</h2>
    </section>

    <section class="front-cover">
      <div class="cover-art" role="img" aria-label="Officer's hand firing a handgun with a bright muzzle flash, seen from behind the shooter against a blue uniform"></div>
      <h1 class="title-block">
        <span class="title-initials">R.K.T.</span>
        <span class="title-line-1">BEYOND</span>
        <span class="title-line-2">THE</span>
        <span class="title-line-3">SILENCE</span>
        <span class="title-line-4">FELL</span>
      </h1>
      <div class="author-row">
        <svg class="badge-shape" viewBox="0 0 104 118" role="img" aria-label="Silver police badge">
          <defs>
            <linearGradient id="badgeSilver" x1="0" y1="0" x2="1" y2="1">
              <stop offset="0" stop-color="#f1f4f7"/>
              <stop offset=".5" stop-color="#8a96a2"/>
              <stop offset="1" stop-color="#dfe5ea"/>
            </linearGradient>
          </defs>
          <path d="M52 4 L88 18 L96 52 L84 92 L52 114 L20 92 L8 52 L16 18 Z" fill="url(#badgeSilver)" stroke="#6e7a86" stroke-width="2"/>
        </svg>
        <span class="author-name">AUTHOR NAME</span>
      </div>
    </section>
  </main>
</body>
</html>
```